2 x Digitize Logo | 2 x Business Cards | 2 x Fridge Magnets

We require 6 deliverables:
1. Residential logo redrawn (same just high quality for large print format).
2. Corporate logo redrawn (minor changes to wording and high quality for large print format).
3. New business card design for Furniture Removals (residential)
4. New business card design for Corporate Relocations (business)
5. New Fridge magnet for Furniture removals (residential)
6. New fridge magnet for Corporate Relocations (business)
1. Residential Logo
a. We require the logo to be translated into a high quality digital image with no modifications.
2. Residential Logo
a. We require the logo to be edited (add the word corporate relocations) be translated into a high quality digital image.
3. Using the resilogo please make a new business card for our business.
a. Please see the web site https://www.brightlanehaulage.com.au for colours and inspiration.
b. The residential business card needs the following information:
i. Business Name (using the residential logo).
ii. Free Call: 1800 BL Haul (the Q, P and Move much be the same colour as the logo).
iii. Website: www.BrightLaneHaulage.com.au
iv. Address: 4/7 Ashgrove Court, VIC 3521
v. Email: move@BrightLaneHaulage.com.au
vi. backof Card:
Review our service
www.RateYourStay.com.au
Services: Local, Country, Interstate | Furniture Removals | Piano, Billiard Tables & Antiques
4. Using the corplogo please make a new business card for our business.
b. The corporate business card needs the following information:
i. Business Name (using the corporate logo).
v. Email: corporate@BrightLaneHaulage.com.au
vi. Back of Card:
Review our service
www.RateYourStay.com.au
Services: Corporate relocations | Office equipment moves | Packing Service | Packing Materials
5. Using the resilogo please make a new fridge magent for our business.
b. The residential fidge magnet needs the following information:
iv. Services: Local, Country, Interstate | Furniture Removals | Piano, Billiard Tables & Antiques
6. Using the corplogo please make a new fridge magent for our business.
b. The corporate fidge magnet needs the following information:
iv. Services: Local, Country, Interstate | Corporate relocations
Target Market(s)
Residential Furniture Removals and Corporate Office relocations
Industry/Entity Type
Business
Contact Information for Business Card
Please see full brief for six items required
Requirements
Must have
- Clean simple, easy to read
Nice to have
- fresh, stand out, eye catching
Should not have
- plain, standard, boring, general

```html
<!DOCTYPE html>
<html lang="en">
<head>
<meta charset="utf-8">
<title>Bright Lane Haulage – Cards and Magnets</title>
<link rel="stylesheet" href="https://fonts.googleapis.com/css2?family=Exo+2:wght@400;500;600;800&family=Open+Sans:wght@400;600&family=Tinos:wght@700&display=swap">
<style>
  :root{
    --bg:#dcdddf;
    --white:#ffffff;
    --ink:#1f1f1f;
    --sunshine:#fdc714;
    --poppy:#ed2029;
    --meadow:#27b04b;
    --brick:#be1f29;
    --forest:#007a3d;
  }
  *{margin:0;padding:0;box-sizing:border-box}
  html,body{width:1195px;height:1200px;overflow:hidden;background:var(--bg)}
  body{position:relative;font-family:"Exo 2",sans-serif;color:var(--ink)}
  .card{position:absolute;width:492px;height:303px;background:var(--white);overflow:hidden}
  .card--rounded{border-radius:20px}
  .card svg.backdrop{position:absolute;inset:0;width:100%;height:100%}

  /* residential front */
  .resi-front{left:84px;top:84px;text-align:center}
  .resi-front .brand{position:absolute;top:52px;left:0;right:0;font-weight:800;font-size:38px;color:var(--poppy);letter-spacing:1px;text-transform:uppercase}
  .resi-front .contact{position:absolute;left:0;right:0;font-weight:600;font-size:18px;letter-spacing:.4px}
  .resi-front .label{font-weight:400;font-size:11.5px;text-transform:uppercase}
  .resi-front .office{font-weight:400;font-size:16px}
  .stripe{position:absolute;bottom:0;height:18px}
  .stripe--yellow{left:0;width:166px;background:var(--sunshine)}
  .stripe--red{left:166px;width:112px;background:var(--poppy)}
  .stripe--green{left:278px;width:214px;background:var(--meadow)}

  /* residential back */
  .resi-back{left:618px;top:84px}
  .colour-block{position:absolute;top:0;height:204px}
  .colour-block--yellow{left:0;width:166px;background:var(--sunshine)}
  .colour-block--red{left:166px;width:113px;background:var(--poppy)}
  .colour-block--green{left:279px;width:213px;background:var(--meadow)}
  .resi-back .brand{position:absolute;top:84px;left:0;right:0;text-align:center;font-weight:800;font-size:40px;color:var(--white);text-transform:uppercase;letter-spacing:1px}
  .resi-back .review{position:absolute;right:260px;top:236px;text-align:right;font-size:12.5px;line-height:17px}
  .resi-back .review strong{font-weight:600;font-size:14px}
  .resi-back .divider{position:absolute;left:248px;top:222px;width:1px;height:62px;background:#777}
  .resi-back .services{position:absolute;left:262px;top:222px;font-size:12px;line-height:17px}
  .resi-back .services h3{font-size:12.5px;font-weight:600}
  .resi-back ul{list-style:none}
  .resi-back li::before{content:"• "}

  /* corporate pieces */
  .corp{font-family:"Open Sans",sans-serif}
  .corp-front{left:84px;top:640px}
  .corp-front .brand{position:absolute;left:18px;top:136px;width:118px;text-align:center;font-family:"Tinos",serif;font-weight:700;font-size:13px;line-height:16px;color:var(--brick)}
  .corp-front .contact{position:absolute;left:157px;font-size:11.5px;text-transform:uppercase;white-space:nowrap}
  .corp-front .contact b{font-family:"Tinos",serif;font-weight:700;font-size:15.5px;text-transform:none}
  .corp-title{position:absolute;left:0;right:0;text-align:center}
  .corp-title .name{font-family:"Tinos",serif;font-weight:700;font-size:32px;color:var(--brick);line-height:36px;text-transform:uppercase}
  .corp-title .tagline{font-size:30px;color:var(--forest);line-height:38px}
  .corp-title .tagline span{color:var(--brick)}
  .corp .services-head{font-family:"Tinos",serif;font-weight:700;font-size:12.5px;text-transform:uppercase}
  .corp .svc{position:absolute;font-size:12px;white-space:nowrap}
  .corp .svc::before{content:"• "}
  .magnet-a{left:618px;top:468px}
  .magnet-a .review{position:absolute;right:18px;top:24px;text-align:right;font-size:12px;line-height:20px}
  .magnet-a .review b{font-family:"Tinos",serif;font-size:15.5px}
  .magnet-b{left:618px;top:813px}
  .magnet-b .on-red{color:var(--white)}
  .magnet-b .svc{font-weight:600}
  .magnet-b .review{position:absolute;left:22px;top:240px;color:var(--white);font-size:12px;line-height:20px;font-weight:600}
  .magnet-b .review b{font-family:"Tinos",serif;font-size:15.5px}
</style>
</head>
<body>

<!-- Residential business card: front -->
<section class="card card--rounded resi-front">
  <div class="brand">Bright Lane Haulage</div>
  <p class="contact" style="top:142px"><span class="label">Free call:</span> 1800 BL Haul</p>
  <p class="contact" style="top:168px"><span class="label">Visit:</span> www.BrightLaneHaulage.com.au</p>
  <p class="contact" style="top:194px"><span class="label">Email:</span> move@BrightLaneHaulage.com.au</p>
  <p class="contact office" style="top:250px"><span class="label">Office:</span> 4/7 Ashgrove Court, VIC 3521</p>
  <div class="stripe stripe--yellow"></div>
  <div class="stripe stripe--red"></div>
  <div class="stripe stripe--green"></div>
</section>

<!-- Residential business card: back -->
<section class="card card--rounded resi-back">
  <div class="colour-block colour-block--yellow"></div>
  <div class="colour-block colour-block--red"></div>
  <div class="colour-block colour-block--green"></div>
  <div class="brand">Bright Lane Haulage</div>
  <p class="review">Review our service<br><strong>www.RateYourStay.com.au</strong></p>
  <div class="divider"></div>
  <div class="services">
    <h3>SERVICES</h3>
    <ul>
      <li>Local, Country, Interstate</li>
      <li>Furniture Removals</li>
      <li>Piano, Billiard Tables &amp; Antiques</li>
    </ul>
  </div>
</section>

<!-- Corporate business card: front -->
<section class="card corp corp-front">
  <svg class="backdrop" viewBox="0 0 616 379" preserveAspectRatio="none" aria-hidden="true">
    <polygon points="0,0 575,0 365,103 0,103" fill="var(--brick)"/>
    <polygon points="616,16 616,82 590,103 445,103" fill="var(--forest)"/>
    <polygon points="0,262 285,262 395,379 0,379" fill="var(--brick)"/>
    <polygon points="315,262 432,262 440,292 473,379 410,379" fill="var(--forest)"/>
    <rect x="0" y="103" width="616" height="3" fill="#e4e4e4"/>
    <rect x="0" y="259" width="616" height="3" fill="#e4e4e4"/>
  </svg>
  <div class="brand">BRIGHT LANE HAULAGE</div>
  <p class="contact" style="top:114px">Free call: <b>1800 BL Haul</b></p>
  <p class="contact" style="top:138px">Visit: <b>www.BrightLaneHaulage.com.au</b></p>
  <p class="contact" style="top:161px">Email: <b>corporate@BrightLaneHaulage.com.au</b></p>
  <p class="contact" style="top:184px">Office: <b>4/7 Ashgrove Court, VIC 3521</b></p>
</section>

<!-- Corporate fridge magnet: review on top -->
<section class="card corp magnet-a">
  <svg class="backdrop" viewBox="0 0 616 379" preserveAspectRatio="none" aria-hidden="true">
    <polygon points="0,0 275,0 70,103 0,103" fill="var(--brick)"/>
    <polygon points="272,0 392,0 272,103 137,103" fill="var(--forest)"/>
    <polygon points="0,283 95,379 0,379" fill="var(--brick)"/>
    <polygon points="0,263 160,263 133,296 173,379 120,379 0,270" fill="var(--forest)"/>
    <rect x="0" y="103" width="616" height="3" fill="#e4e4e4"/>
    <rect x="0" y="260" width="616" height="3" fill="#e4e4e4"/>
  </svg>
  <p class="review">Review our service<br><b>www.RateYourStay.com.au</b></p>
  <div class="corp-title" style="top:112px">
    <div class="name">Bright Lane Haulage</div>
    <div class="tagline">CORPORATE <span>RELOCATIONS</span></div>
  </div>
  <div class="services-head" style="position:absolute;left:164px;top:233px">Services</div>
  <p class="svc" style="left:164px;top:250px">Corporate relocations</p>
  <p class="svc" style="left:322px;top:250px">Office Equipment Moves</p>
  <p class="svc" style="left:164px;top:268px">Packing Service</p>
  <p class="svc" style="left:322px;top:268px">Packing Materials</p>
</section>

<!-- Corporate fridge magnet: services on top -->
<section class="card corp magnet-b">
  <svg class="backdrop" viewBox="0 0 616 379" preserveAspectRatio="none" aria-hidden="true">
    <polygon points="0,0 575,0 365,103 0,103" fill="var(--brick)"/>
    <polygon points="616,16 616,82 590,103 445,103" fill="var(--forest)"/>
    <polygon points="0,262 285,262 395,379 0,379" fill="var(--brick)"/>
    <polygon points="315,262 432,262 440,292 473,379 410,379" fill="var(--forest)"/>
    <rect x="0" y="103" width="616" height="3" fill="#e4e4e4"/>
    <rect x="0" y="259" width="616" height="3" fill="#e4e4e4"/>
  </svg>
  <div class="services-head on-red" style="position:absolute;left:18px;top:20px">Services</div>
  <p class="svc on-red" style="left:18px;top:37px">Corporate relocations</p>
  <p class="svc on-red" style="left:175px;top:37px">Office Equipment Moves</p>
  <p class="svc on-red" style="left:18px;top:56px">Packing Service</p>
  <p class="svc on-red" style="left:175px;top:56px">Packing Materials</p>
  <div class="corp-title" style="top:112px">
    <div class="name">Bright Lane Haulage</div>
    <div class="tagline">CORPORATE <span>RELOCATIONS</span></div>
  </div>
  <p class="review">Review our service<br><b>www.RateYourStay.com.au</b></p>
</section>

</body>
</html>
```